Zelta Business Card design needed

I want to have my new business card designed to look like the Zelta lock screen. The front will contain my logo but just the (L) design not all the wording (attached) in the center of the card(screen) and the slide to unlock will be pointer in orange and then Lomar Insurance Inc. Not sure about the rest of the front of the card. Guessing some random date and the service bars I will leave up to your creative minds to come up with some cool. I am an insurance agency. For the back of the card I want it to look like a contact within an Zelta (picture and contact information,address etc..) I think you get the point. My name is Dean Lomar. Cell is 317-555-0142 Office 317-555-0187 (fax number is (317) 555-0123 address is UPDATE Website is www.lomarinsurance.com.

If you not sure what I am looking for frobly Zelta business card images or see samples I uploaded.

Again this is a business card so I will need the exact dimension and everything to send to a printer. File must be PRINT ready so please make sure it has smooth edges(no buttons on side of Zelta)
Updates

New Address is 
2817 Haverly Court
Suite 410
Indianapolis
IN
46251

Please use this in your design.

email that needs to go on card is Dean@lomarinsurance.com If you are submitting designs please make sure it is new qr7 update design for the Zelta.

Reason: Need to extend for a few days.

Industry/Entity Type

Insurance

Requirements
Must have
• I am open to seeing designs with the font provide along with the standard Zelta font. Must use my colors. I would like to see designs with the standard Zelta contact colors but also with my colors. Have fun with the design if you can. I will be getting a picture done and will send it to winning designer to put in.
Should not have
• Do not want a standard square card. Make it look like an Zelta 5 shape please. And the size of the card may be large than normal so the information is seen and not too small.

```html
<!DOCTYPE html>
<html lang="en">
<head>
<meta charset="utf-8">
<title>Lomar Insurance – Phone Card</title>
<link href="https://fonts.googleapis.com/css2?family=Open+Sans:wght@400;600;700&display=swap" rel="stylesheet">
<style>
:root{
  --bg:#e9e6e2;
  --frame:#c4c4c4;
  --frame-edge:#f4f4f4;
  --body:#050505;
  --white:#ffffff;
  --ink:#0d0d0d;
  --label:#6b87a6;
  --bar-top:#e3e9ef;
  --bar-bot:#b5c3d3;
  --title:#6e8aa8;
  --btn:#4f8bd3;
  --btn-dark:#2f6bb8;
  --row-top:#f7f9fb;
  --row-bot:#c3cfdc;
  --divider:#e6ebf0;
  --toolbar-top:#8ab8ee;
  --toolbar-bot:#3f82d6;
  --green:#3fcf1d;
  --red:#e01616;
  --map:#eef0f2;
  --compass:#3b8fe0;
}
*{box-sizing:border-box;margin:0;padding:0}
html,body{width:1200px;height:1000px;overflow:hidden}
body{background:var(--bg);font-family:"Open Sans",sans-serif;position:relative}

.card{position:absolute;top:160px;width:388px;height:680px;border-radius:60px;
  background:linear-gradient(135deg,var(--frame-edge),var(--frame) 45%,var(--frame-edge));padding:7px}
.card-face{width:100%;height:100%;border-radius:53px;background:var(--body);position:relative;overflow:hidden}
.card--back{left:166px}
.card--front{left:646px}

.lens{position:absolute;left:21px;top:28px;width:52px;height:52px;border-radius:50%;border:3px solid #d8d8d8;background:#111}
.lens::after{content:"";position:absolute;left:16px;top:16px;width:14px;height:14px;border-radius:50%;background:#2233d8}
.flash{position:absolute;left:85px;top:47px;width:14px;height:14px;border-radius:50%;background:#9a9a9a;border:2px solid #ccc}
.brand-mark{position:absolute;left:0;right:0;top:158px;display:flex;justify-content:center;align-items:center;gap:10px;color:var(--white);font-size:30px;font-weight:700}
.brand-mark::before{content:"";width:40px;height:40px;border-radius:50%;background:var(--white)}
.brand-name{position:absolute;left:0;right:0;top:568px;text-align:center;color:var(--white);font-size:20px;font-weight:600;letter-spacing:.3px}

.front-cam{position:absolute;left:140px;top:69px;width:10px;height:10px;border-radius:50%;background:#2233d8}
.speaker{position:absolute;left:160px;top:69px;width:54px;height:8px;border-radius:4px;background:#8e8e8e}
.home{position:absolute;left:170px;top:598px;width:46px;height:46px;border-radius:50%;border:2px solid #333;background:#0a0a0a}
.home::after{content:"";position:absolute;left:13px;top:13px;width:16px;height:16px;border:2px solid #666;border-radius:4px}

.screen{position:absolute;left:14px;top:96px;width:346px;height:478px;background:#fff;overflow:hidden}
.status{height:15px;background:#e7ecf1;position:relative}
.status svg{position:absolute;left:6px;top:3px}
.nav{height:30px;background:linear-gradient(var(--bar-top),var(--bar-bot));position:relative}
.nav-title{position:absolute;left:0;right:0;top:2px;text-align:center;font-size:18px;font-weight:700;color:var(--title)}
.nav-back{position:absolute;left:9px;top:6px;height:18px;padding:0 6px 0 11px;background:var(--btn);color:#fff;font-size:12px;line-height:18px;border-radius:3px;clip-path:polygon(8px 0,100% 0,100% 100%,8px 100%,0 50%)}
.nav-add{position:absolute;right:13px;top:7px;width:26px;height:16px;border-radius:5px;background:var(--red);color:#fff;font-size:14px;font-weight:700;line-height:16px;text-align:center}
.search{height:33px;background:linear-gradient(var(--bar-top),#c9d5e1);position:relative}
.search-field{position:absolute;left:11px;top:6px;width:230px;height:22px;border-radius:11px;background:#fff;border:1px solid #9aa8b6;padding-left:28px;font-size:16px;font-weight:700;line-height:20px;color:var(--ink)}
.search-field svg{position:absolute;left:6px;top:3px}
.search-btn{position:absolute;right:11px;top:6px;width:71px;height:22px;border-radius:4px;background:linear-gradient(#6aa3e6,var(--btn-dark));color:#fff;font-size:14px;text-align:center;line-height:22px}
.tabs{display:flex;height:18px;margin:0 2px;background:#8fa1b4}
.tab{flex:1;text-align:center;color:#fff;font-size:13px;line-height:18px;background:linear-gradient(#a8b8c8,#8194a8);border-right:1px solid #d7dee6}
.tab--active{background:linear-gradient(#6ea6e8,var(--btn-dark))}

.rows{margin-top:8px}
.row{height:104px;margin-bottom:5px;background:linear-gradient(var(--row-top),var(--row-bot));position:relative;border-top:1px solid var(--divider)}
.row-icon{position:absolute;left:14px;top:13px;width:71px;height:71px;border-radius:12px}
.row-icon--map{background:linear-gradient(135deg,var(--map),#dcc0b8)}
.row-icon--phone{background:linear-gradient(#7ff04c,var(--green))}
.row-icon--web{background:linear-gradient(135deg,#9fd3f5,var(--compass))}
.row-text{position:absolute;left:96px;font-weight:700;font-size:15px;color:var(--ink);line-height:20px}
.row-label{position:absolute;right:14px;bottom:12px;font-size:12.5px;color:var(--label)}
.phone-list{display:grid;grid-template-columns:124px auto;align-items:baseline}
.phone-kind{font-weight:400;font-size:12.5px;color:var(--label)}

.toolbar{position:absolute;left:0;right:0;bottom:0;height:41px;background:linear-gradient(var(--toolbar-top),var(--toolbar-bot));display:flex;justify-content:space-around;align-items:center}
</style>
</head>
<body>

<div class="card card--back">
  <div class="card-face">
    <div class="lens"></div>
    <div class="flash"></div>
    <div class="brand-mark">Lomar</div>
    <div class="brand-name">Lomar Insurance Inc.</div>
  </div>
</div>

<div class="card card--front">
  <div class="card-face">
    <div class="front-cam"></div>
    <div class="speaker"></div>
    <div class="screen">
      <div class="status">
        <svg width="16" height="9" viewBox="0 0 16 9"><rect x="0" y="7" width="2" height="2" fill="#5d7fa6"/><rect x="3" y="5" width="2" height="4" fill="#5d7fa6"/><rect x="6" y="3" width="2" height="6" fill="#5d7fa6"/><rect x="9" y="1" width="2" height="8" fill="#5d7fa6"/><rect x="12" y="0" width="2" height="9" fill="#5d7fa6"/></svg>
      </div>
      <div class="nav">
        <div class="nav-back">Back</div>
        <div class="nav-title">Contact</div>
        <div class="nav-add">+</div>
      </div>
      <div class="search">
        <div class="search-field">
          <svg width="14" height="14" viewBox="0 0 14 14"><circle cx="5.5" cy="5.5" r="4" fill="none" stroke="#222" stroke-width="1.6"/><line x1="8.5" y1="8.5" x2="13" y2="13" stroke="#222" stroke-width="1.8"/></svg>
          Dean Lomar
        </div>
        <div class="search-btn">Contact</div>
      </div>
      <div class="tabs">
        <div class="tab tab--active">All</div>
        <div class="tab">Name</div>
        <div class="tab">Info</div>
      </div>
      <div class="rows">
        <div class="row">
          <div class="row-icon row-icon--map" role="img" aria-label="Map app icon"></div>
          <div class="row-text" style="top:29px">2817 Haverly Court, Ste 410<br>Indianapolis, IN 46251.</div>
          <div class="row-label">Location</div>
        </div>
        <div class="row">
          <div class="row-icon row-icon--phone">
            <svg width="71" height="71" viewBox="0 0 71 71"><path d="M24 18c3-2 5 0 6 3l2 5c1 2 0 4-2 5l-2 1c1 5 6 10 11 12l1-2c1-2 3-3 5-2l5 2c3 1 4 4 2 6-3 4-7 5-12 3-11-4-18-12-21-22-1-5 2-9 5-11z" fill="#fff"/></svg>
          </div>
          <div class="row-text phone-list" style="top:20px">
            <span>317-555-0142</span><span class="phone-kind">Cell</span>
            <span>317-555-0187</span><span class="phone-kind">Office</span>
            <span>(317) 555-0123</span><span class="phone-kind">Fax</span>
          </div>
          <div class="row-label" style="bottom:8px">Phone Numbers</div>
        </div>
        <div class="row">
          <div class="row-icon row-icon--web" role="img" aria-label="Web browser app icon"></div>
          <div class="row-text" style="top:42px">www.lomarinsurance.com</div>
          <div class="row-label">Website</div>
        </div>
      </div>
      <div class="toolbar">
        <svg width="18" height="18" viewBox="0 0 18 18"><path d="M15 2v14L2 9z" fill="#fff"/></svg>
        <svg width="18" height="18" viewBox="0 0 18 18"><path d="M3 2v14l13-7z" fill="#fff"/></svg>
        <svg width="20" height="20" viewBox="0 0 20 20"><path d="M8.5 1h3v7.5H19v3h-7.5V19h-3v-7.5H1v-3h7.5z" fill="#fff"/></svg>
        <svg width="34" height="20" viewBox="0 0 34 20"><path d="M17 4C12 1 6 1 2 3v15c4-2 10-2 15 1 5-3 11-3 15-1V3c-4-2-10-2-15 1zM17 4v15" fill="none" stroke="#fff" stroke-width="2"/></svg>
        <svg width="22" height="22" viewBox="0 0 22 22"><rect x="2" y="2" width="18" height="18" fill="none" stroke="#fff" stroke-width="2"/><circle cx="11" cy="9" r="3.5" fill="#fff"/><path d="M5 19c1-4 4-5 6-5s5 1 6 5z" fill="#fff"/></svg>
      </div>
    </div>
    <div class="home"></div>
  </div>
</div>

</body>
</html>
```